Velmora Harbor Church Direct Mail Postcard

We are launching a new church in Olathe Kansas (Kansas City suburb). People here are well educated and pretty affluent. There are many young families which is our mail target demo. We need a 6 inch by 11 inch postcard that will be for a mass mailer that will coincide with our launch. The goal is simply to get people to come to the church launch which is September 18th. We think the theme should be "What in Heaven are you here for?" or "God is not Mad at you..No Matter What?" or "The truth is...you matter." It needs to include a map to our church which is inside Copper Ridge Middle School: 18400 W 93rd St, Olathe, KS 66047. Service is at 10:00 am, Safe childcare is provided from infants up to 12 year olds. There should be some space for us to put in some messaging and bullets. Possibly include a few pictures of happy families and people worshiping. I’ve attached our Logo, but we actually need to flip the colors so that the blue arrow is on top and pointing down, and the gray arrow is pointing up.

Target Market(s)

Young Families

Industry/Entity Type

Church

Requirements
Must have
• Post Card should be front and back full color
• Our website clearly shown on the back: VelmoraHarborChurch.com
• There should be a small map on the back with our location.
• It should say our service starts at 10:00 and that we our first service is Sept 18th
• The message or images on the front are there primarily to get people to turn the card over. UPDATE: We like the idea "What in Heaven are you here for?" on the front the best, followed by "God is NOT Mad at you..." (front) "no matter what" (back) second, and then "The truth is.." (front) "You matter" back third.
• Only 1 of the themes should be used at a time. So for example, the front should say, "What In Heaven are you here for?" or "God is not mad at you..." but not both.
• We like clean, modern looks. Don't put the logo on the front.
Nice to have
• Some stock photos of families or people worshipping (contemporary charismatic church)
• I attached some examples of cards that worked well for other churches. Please check them out.
Should not have
• The words "Grand Opening"

```html
<!DOCTYPE html>
<html lang="en">
<head>
<meta charset="utf-8">
<title>Velmora Harbor Church – Launch Postcard</title>
<link rel="stylesheet" href="https://fonts.googleapis.com/css2?family=Bebas+Neue&family=Archivo:wght@800&family=Open+Sans:wght@400;600;700&family=Roboto+Condensed:wght@700&display=swap">
<style>
  :root {
    --brand-blue: #0a44f2;
    --ink: #2b2b2b;
    --white: #ffffff;
    --paper: #f2f2f4;
    --canvas: #ffffff;
    --sky-light: #f6efe2;
    --sky-blue: #a9c6e8;
    --stamp: #d6d6d6;
    --pin-red: #b3211b;
  }
  * { margin: 0; padding: 0; box-sizing: border-box; }
  html, body { width: 1200px; height: 1200px; overflow: hidden; background: var(--canvas); }
  .stage { position: relative; width: 1200px; height: 1200px; }

  /* ---------- Front ---------- */
  .card-front {
    position: absolute; left: 421px; top: 53px; width: 359px; height: 655px;
    overflow: hidden;
    box-shadow: 0 4px 10px rgba(0,0,0,.18);
  }
  .front-sky {
    position: absolute; inset: 0;
    background:
      radial-gradient(ellipse 60% 22% at 50% 88%, #fff8e6 0%, rgba(255,248,230,0) 100%),
      linear-gradient(180deg, #b9823d 0%, #e3c89e 14%, var(--sky-light) 30%, #f4f2ee 45%, #dbe6f3 62%, var(--sky-blue) 74%, #e9e4dc 84%, #e3a556 94%, #b86a23 100%);
  }
  .front-word {
    position: absolute; font-family: "Bebas Neue", "Oswald", sans-serif;
    color: var(--ink); line-height: 1; white-space: nowrap;
  }
  .front-word--what { left: 46px; top: 163px; font-size: 98px; }
  .front-word--are { left: 46px; top: 327px; font-size: 76px; }
  .front-band {
    position: absolute; background: var(--brand-blue); color: var(--white);
    font-family: "Archivo", "Arial Black", sans-serif; font-weight: 800;
    line-height: 1; white-space: nowrap; display: flex; align-items: center;
  }
  .front-band--heaven { left: 39px; top: 247px; width: 320px; height: 67px; padding-left: 6px; font-size: 47px; }
  .front-band--here { left: 0; top: 397px; width: 319px; height: 58px; padding-left: 45px; font-size: 43px; letter-spacing: -0.3px; }

  /* ---------- Back ---------- */
  .card-back {
    position: absolute; left: 272px; top: 774px; width: 658px; height: 358px;
    overflow: hidden; background: var(--paper);
    box-shadow: 0 4px 10px rgba(0,0,0,.18);
    font-family: "Open Sans", sans-serif;
  }
  .photo { position: absolute; top: 0; height: 106px; }
  .photo--worship { left: 0; width: 190px; background: linear-gradient(160deg, #e9ecef 0%, #f7f7f5 55%, #e6b9a6 100%); }
  .photo--prayer { left: 194px; width: 190px; background: linear-gradient(150deg, #f1e6c4 0%, #c98f63 55%, #7a2e1f 100%); }
  .map {
    position: absolute; left: 386px; top: 0; width: 272px; height: 108px;
    background: linear-gradient(180deg, #e6e4df 0%, #efede9 100%);
  }
  .map-pin { position: absolute; left: 116px; top: 40px; width: 14px; height: 20px; }
  .map-label {
    position: absolute; left: 132px; top: 58px; font-size: 8px; font-weight: 700;
    color: var(--pin-red); line-height: 1.1;
  }
  .map-address {
    position: absolute; left: 414px; top: 91px; font-family: "Roboto Condensed", sans-serif;
    font-size: 7.6px; font-weight: 700; color: #111; white-space: nowrap;
  }

  .childcare-band {
    position: absolute; left: 0; top: 106px; width: 400px; height: 98px;
    background: var(--brand-blue);
  }
  .childcare-text {
    position: absolute; left: 26px; top: 123px; color: var(--white);
    font-family: "Bebas Neue", sans-serif; font-size: 33px; letter-spacing: -0.5px;
    line-height: 33px; white-space: nowrap;
  }
  .service-band {
    position: absolute; left: 402px; top: 108px; width: 256px; height: 58px;
    background: var(--brand-blue); color: var(--white); text-align: center;
    font-family: "Bebas Neue", sans-serif; line-height: 1; white-space: nowrap;
  }
  .service-time { display: block; font-size: 33px; letter-spacing: -0.5px; margin-top: 5px; }
  .service-site { display: block; font-size: 20px; }

  .launch-headline {
    position: absolute; left: 27px; top: 220px; color: var(--ink);
    font-family: "Bebas Neue", sans-serif; font-size: 27px; letter-spacing: -0.5px;
    font-weight: 400; line-height: 1; white-space: nowrap;
  }
  .launch-bullets {
    position: absolute; left: 34px; top: 264px; list-style: none;
    font-size: 8.2px; line-height: 10.5px; color: #333;
  }
  .launch-bullets li { position: relative; padding-left: 13px; }
  .launch-bullets li::before {
    content: ""; position: absolute; left: 0; top: 2.5px; width: 5.5px; height: 5.5px;
    border-radius: 50%; background: var(--brand-blue);
  }
  .launch-message {
    position: absolute; left: 174px; top: 264px; width: 192px; height: 56px;
    border: 2px solid var(--brand-blue); border-radius: 12px;
    font-size: 7.4px; line-height: 9px; color: #333; text-align: center;
    display: flex; align-items: center; justify-content: center; padding: 0 8px;
  }
  .bottom-bar { position: absolute; left: 0; top: 342px; width: 658px; height: 16px; background: var(--brand-blue); }
  .divider { position: absolute; inset: 0; width: 658px; height: 358px; pointer-events: none; }

  .church-name {
    position: absolute; left: 426px; top: 206px; display: flex; align-items: center; gap: 4px;
    font-family: "Bebas Neue", sans-serif; font-size: 15px; color: var(--brand-blue); white-space: nowrap;
  }
  .church-name__mark { width: 8px; height: 8px; background: var(--brand-blue); }
  .stamp-box { position: absolute; left: 584px; top: 184px; width: 52px; height: 52px; background: var(--stamp); }
</style>
</head>
<body>
<main class="stage">

  <section class="card-front" aria-label="Postcard front">
    <div class="front-sky" role="img" aria-label="Golden heavenly sky with glowing clouds and stars above shimmering water"></div>
    <span class="front-word front-word--what">WHAT</span>
    <div class="front-band front-band--heaven">IN HEAVEN</div>
    <span class="front-word front-word--are">ARE YOU</span>
    <div class="front-band front-band--here">HERE FOR?</div>
  </section>

  <section class="card-back" aria-label="Postcard back">
    <div class="photo photo--worship" role="img" aria-label="Photo of a person raising hands in worship"></div>
    <div class="photo photo--prayer" role="img" aria-label="Photo of hands folded in prayer on an open Bible"></div>

    <div class="map" role="img" aria-label="Small street map showing Copper Ridge Middle School">
      <svg class="map-pin" viewBox="0 0 14 20" aria-hidden="true">
        <path d="M7 0C3.1 0 0 3.1 0 7c0 5 7 13 7 13s7-8 7-13C14 3.1 10.9 0 7 0z" fill="#e0392b"/>
        <circle cx="7" cy="7" r="2.6" fill="#8c1a12"/>
      </svg>
      <div class="map-label">Copper Ridge<br>Middle School</div>
    </div>

    <div class="childcare-band"></div>
    <p class="childcare-text">Safe childcare is provided<br>from infants up to 12 year olds</p>

    <h2 class="launch-headline">A new church, starting September 18th</h2>
    <ul class="launch-bullets">
      <li>Lorem ipsum dolor sit amet</li>
      <li>Lorem ipsum dolor sit</li>
      <li>Lorem ipsum dolor sit am</li>
      <li>Lorem ipsum dolor sita</li>
      <li>Lorem ipsum dolor sit amet</li>
    </ul>
    <div class="launch-message">Lorem ipsum dolor sit ametLorem ipsum dolor sit ametLorem ipsum dolor sit ametLorem ipsum dolor sit ametLorem ipsum dolor sit ametLorem ipsum dolor sit amet</div>

    <svg class="divider" viewBox="0 0 658 358" aria-hidden="true">
      <rect x="190" y="0" width="4" height="106" fill="#0a44f2"/>
      <polygon points="384,0 390,0 418,342 412,342" fill="#ffffff"/>
      <polygon points="378,0 385,0 413,342 406,342" fill="#0a44f2"/>
    </svg>

    <div class="map-address">Copper Ridge Middle School: 18400 W 93rd St, Olathe, KS 66047</div>

    <div class="service-band">
      <span class="service-time">Service is at 10:00 AM</span>
      <span class="service-site">VelmoraHarborChurch.com</span>
    </div>

    <div class="church-name"><span class="church-name__mark"></span>Velmora Harbor Church</div>
    <div class="stamp-box"></div>

    <div class="bottom-bar"></div>
  </section>

</main>
</body>
</html>
```